Post Card Notification - rental property registration

We need a post card mailer designed to notify Landlord's of the need to register their rental properties according to local ordinance. Designed for optimal response, the response we are looking for is getting the recipient to go to a URL that will be on the postcard.

The postcards will be sent on behalf on Municipalities (aka communities) that we represent. They notify the Homeowner/Landlord of the need to register their property. We will inform them of the properties we have discovered evidence and registration is required. We are considering a color post card that will include the community logo and the company logo and other formatting graphics that enhance the design to get the result we are looking for.

There will be dynamic content in the design that will be specific tothe community logo, message text, property addresses, URL/Code, etc...

Clarifications 9/10/2018:
I wanted to clarify that this post card is not an advertisement but rather an official notification of the obligation to comply and register the property. We want the design to be professional but not to look like an advertisement.

We are looking for instant credibility. This should come with a focus on the community logo. Whether or not we even show the VELTRIDANE logo is optional, I am open to designs without it.

Also, we want to emphasize getting them to the coded link.

None of the designs so far achieve the instant credibility or give enough focus to the getting them to the link.

Lastly, the property list will be an actual list of 1 to 5 properties that are required to be registered by the owner. The design should contemplate an actual list of properties.

If you need a sample community logo you can pull one from veltridane.example or from any U.S. community home page.

One other point of clarification, the postcard will be sent for one community at a time. I see some designs with multiple community logos and that is not accurate. If an owner has rental properties in multiple communities then they will get multiple postcards from us. Each post card will be unique to a specific community.

If the owner has multiple properties in that community then they will be listed (hence the property list of 1 to 5 properties)

Most of the designs I am reviewing have focused to much on making it look like an advertisement with property images. I wanted to clarify that this should look official. There will be a community logo on the post card. We may not even have the VELTRIDANE logo on the card, I am open to designs with or without it. Also, the property list will be a list of properties where evidence has been found that it is rented by the owner. We anticipate this will be 1 to 5 properties in a dynamic list. The design should contemplate this. We want the design to look professional but it does not need to look like an advertisement. It needs to get their attention, and have them instantly recognize it as official (instant credibility) and get them to go to the link. None of the designs so far give enough prominence to the community logo or link that I think will be necessary to achieve this goal.

Target Market(s)

Landlords of rented properties

Industry/Entity Type

Government

Requirements
Must have
• Must look official, from the communities that we are partnered with
Should not have
• This should not look like a Real Estate advertisement

```html
<!DOCTYPE html>
<html lang="en">
<head>
<meta charset="utf-8">
<title>Rental Registration Notice</title>
<link href="https://fonts.googleapis.com/css2?family=Russo+One&family=Roboto:wght@400;500;700&display=swap" rel="stylesheet">
<style>
:root{
  --navy-deep:#1f3a86;
  --navy:#2b4a9c;
  --navy-ink:#17224a;
  --amber:#f8a402;
  --amber-rule:rgba(255,255,255,.55);
  --white:#ffffff;
}
*{box-sizing:border-box;margin:0;padding:0}
html,body{width:1200px;height:877px;overflow:hidden;background:var(--navy-deep)}
.postcard{position:relative;width:1200px;height:877px;overflow:hidden;font-family:"Roboto",sans-serif;color:var(--white)}
.neighborhood-backdrop{position:absolute;inset:0;background:linear-gradient(135deg,#24438f 0%,#2f52a6 45%,#223c86 100%)}

.brand-name{position:absolute;left:0;width:500px;top:156px;text-align:center;font-weight:500;font-size:46px;letter-spacing:1px;color:var(--white)}

.call-to-action{position:absolute;left:0;width:500px;top:277px;text-align:center}
.cta-lead{font-size:21px;line-height:1.2}
.cta-lead strong{color:var(--amber);font-weight:500;font-size:29px}
.cta-sub{font-size:22px;margin-top:4px}
.cta-go{font-size:21px;font-weight:700;letter-spacing:1px;margin-top:6px}

.link-pointer{position:absolute;left:241px;top:374px}

.registration-link{position:absolute;left:46px;top:462px;width:406px;height:47px;border-radius:10px;background:var(--amber);color:var(--navy-ink);font-family:"Russo One",sans-serif;font-size:21px;display:flex;align-items:center;justify-content:center;letter-spacing:.3px}

.help-text{position:absolute;left:0;width:500px;top:527px;text-align:center;font-size:21px;line-height:29px;letter-spacing:.3px}

.contact-line{position:absolute;display:flex;align-items:center;gap:12px;font-family:"Russo One",sans-serif}
.contact-phone{left:100px;top:602px;font-size:31px;letter-spacing:1px}
.contact-email{left:64px;top:652px;font-size:24px}

.list-heading{position:absolute;left:484px;top:64px;font-family:"Russo One",sans-serif;font-size:26px;letter-spacing:.6px;font-weight:400}

.property-list{position:absolute;left:464px;top:108px;width:736px;background:var(--amber);color:var(--navy-ink);padding-bottom:6px}
.fold-corner{position:absolute;left:0;top:0}
.property-list-title{font-family:"Russo One",sans-serif;font-weight:400;font-size:24px;color:var(--white);padding:10px 0 4px 36px}
.property-entry{display:grid;grid-template-columns:296px 1fr;padding:12px 0 14px;border-top:1px solid var(--amber-rule)}
.property-entry:first-of-type{border-top:none;padding-top:6px}
.entry-owner-col{padding-left:20px;display:flex;flex-direction:column;justify-content:space-between;border-right:2px dotted rgba(255,255,255,.85)}
.entry-site-col{padding-left:20px;padding-right:16px;display:flex;flex-direction:column;gap:12px}
.property-field{font-size:22px;line-height:29px;color:#1c2540}
.property-field b{font-weight:700}
</style>
</head>
<body>
<main class="postcard">
  <div class="neighborhood-backdrop" role="img" aria-label="Aerial view of a residential neighborhood with houses and a cul-de-sac, tinted blue"></div>

  <div class="brand-name">VELTRIDANE</div>

  <div class="call-to-action">
    <p class="cta-lead">To <strong>Register, Exempt</strong> or <strong>Dispute</strong></p>
    <p class="cta-sub">the rental properties on this list.</p>
    <p class="cta-go">GO TO THIS LINK</p>
  </div>

  <svg class="link-pointer" width="18" height="78" viewBox="0 0 18 78" aria-hidden="true">
    <line x1="9" y1="0" x2="9" y2="64" stroke="#f8a402" stroke-width="1.5" stroke-dasharray="3 3"/>
    <polygon points="1,62 17,62 9,76" fill="#f8a402"/>
  </svg>

  <div class="registration-link">WWW.VELTRIDANE.EXAMPLE/101010</div>

  <p class="help-text">If you are having problems with the above<br>link you can contact VELTRIDANE by</p>

  <div class="contact-line contact-phone">
    <svg width="28" height="30" viewBox="0 0 24 24" aria-hidden="true"><path fill="#f8a402" d="M6.6 10.8a15.1 15.1 0 0 0 6.6 6.6l2.2-2.2c.3-.3.7-.4 1-.2 1.1.4 2.3.6 3.6.6.6 0 1 .4 1 1V20c0 .6-.4 1-1 1A17 17 0 0 1 3 4c0-.6.4-1 1-1h3.5c.6 0 1 .4 1 1 0 1.3.2 2.5.6 3.6.1.3 0 .7-.2 1z"/></svg>
    <span>(555) 014-2837</span>
  </div>

  <div class="contact-line contact-email">
    <svg width="32" height="24" viewBox="0 0 32 24" aria-hidden="true"><rect x="1" y="1" width="30" height="22" fill="#f8a402"/><polyline points="1,1 16,13 31,1" fill="none" stroke="#2b4a9c" stroke-width="2"/><path d="M1,23 L12,10 M31,23 L20,10" fill="none" stroke="#2b4a9c" stroke-width="1.5"/></svg>
    <span>support@veltridane.example</span>
  </div>

  <h1 class="list-heading">PROPERTIES REQUIRING RENTAL REGISTRATION:</h1>

  <section class="property-list">
    <svg class="fold-corner" width="26" height="26" viewBox="0 0 26 26" aria-hidden="true"><polygon points="0,24 24,0 24,24" fill="#ffffff"/><polygon points="0,0 24,0 0,24" fill="#2b4a9c"/></svg>
    <h2 class="property-list-title">Property List:</h2>

    <article class="property-entry">
      <div class="entry-owner-col">
        <p class="property-field"><b>Owner Name:</b> Daniel Marsh</p>
        <p class="property-field"><b>PropertyID:</b> #010101</p>
      </div>
      <div class="entry-site-col">
        <p class="property-field"><b>Site Address:</b> House no. 123, street 2, lane 5, city - country (123456)</p>
        <p class="property-field"><b>Notification:</b> Make your registration</p>
      </div>
    </article>

    <article class="property-entry">
      <div class="entry-owner-col">
        <p class="property-field"><b>Owner Name:</b> Daniel Marsh</p>
        <p class="property-field"><b>PropertyID:</b> #010102</p>
      </div>
      <div class="entry-site-col">
        <p class="property-field"><b>Site Address:</b> House no. 48, street 7, lane 2, city - country (123456)</p>
        <p class="property-field"><b>Notification:</b> Make your registration</p>
      </div>
    </article>

    <article class="property-entry">
      <div class="entry-owner-col">
        <p class="property-field"><b>Owner Name:</b> Daniel Marsh</p>
        <p class="property-field"><b>PropertyID:</b> #010103</p>
      </div>
      <div class="entry-site-col">
        <p class="property-field"><b>Site Address:</b> House no. 215, street 4, lane 9, city - country (123456)</p>
        <p class="property-field"><b>Notification:</b> Make your registration</p>
      </div>
    </article>

    <article class="property-entry">
      <div class="entry-owner-col">
        <p class="property-field"><b>Owner Name:</b> Daniel Marsh</p>
        <p class="property-field"><b>PropertyID:</b> #010104</p>
      </div>
      <div class="entry-site-col">
        <p class="property-field"><b>Site Address:</b> House no. 76, street 1, lane 3, city - country (123456)</p>
        <p class="property-field"><b>Notification:</b> Make your registration</p>
      </div>
    </article>

    <article class="property-entry">
      <div class="entry-owner-col">
        <p class="property-field"><b>Owner Name:</b> Daniel Marsh</p>
        <p class="property-field"><b>PropertyID:</b> #010105</p>
      </div>
      <div class="entry-site-col">
        <p class="property-field"><b>Site Address:</b> House no. 302, street 6, lane 8, city - country (123456)</p>
        <p class="property-field"><b>Notification:</b> Make your registration</p>
      </div>
    </article>
  </section>
</main>
</body>
</html>
```